Coral Bay Grins Teeth Whitening Poster and possibly banner as well.

I need a poster and bamner put together for a kiosk stand in the mall we will be renting. I have some pictures. I want the poster to include one of the face and a nice holiday background. I would like it to say -Brighten Your Holiday Smile -Only $89 -Instant Results -Family Owned and Operated. I have a few pics to use or to use as ideas. Also to have our logo somewhere but small and a santa hat to be added to the shark

```html
<!DOCTYPE html>
<html lang="en">
<head>
<meta charset="utf-8">
<title>Coral Bay Grins – Holiday Poster</title>
<link href="https://fonts.googleapis.com/css2?family=Libre+Baskerville:wght@700&family=Lobster+Two:ital,wght@1,700&family=Montserrat:wght@600;700&family=Oswald:wght@600&display=swap" rel="stylesheet">
<style>
  :root {
    --backdrop: #e6e6e6;
    --paper: #ffffff;
    --paper-shade: #f1f1f1;
    --red: #b5162b;
    --sticker-red: #c8102e;
    --curl: #e6e6e6;
    --ink: #222222;
    --navy: #1f4e6a;
    --snow-blue: #1ea1dc;
    --teal: #2290b0;
  }
  * { box-sizing: border-box; margin: 0; padding: 0; }
  html, body { width: 1200px; height: 1200px; overflow: hidden; background: var(--backdrop); }

  .poster {
    position: absolute; left: 103px; top: 0;
    width: 993px; height: 1200px; overflow: hidden;
    background: linear-gradient(160deg, var(--paper) 0%, var(--paper) 55%, var(--paper-shade) 100%);
    font-family: "Montserrat", sans-serif;
  }

  .brand { position: absolute; left: 62px; top: 118px; display: flex; align-items: center; gap: 12px; }
  .brand-dot { width: 50px; height: 50px; border-radius: 50%; background: var(--snow-blue); }
  .brand-name { font-weight: 700; font-size: 22px; color: var(--navy); }

  .decor { position: absolute; }
  .decor-gift { left: 677px; top: 0; width: 316px; height: 262px;
    background: linear-gradient(135deg, #d72a22, #a8160f); }
  .decor-greenery { left: 772px; top: 228px; width: 221px; height: 495px;
    background: linear-gradient(180deg, rgba(46,90,44,.8), rgba(46,90,44,.6) 60%, rgba(46,90,44,.15)); }
  .decor-present { left: 853px; top: 543px; width: 140px; height: 324px;
    background: linear-gradient(90deg, #e9e9e9, #f6f6f6); }

  .polaroid {
    position: absolute; background: var(--paper); padding: 12px 12px 28px;
    box-shadow: 0 6px 14px rgba(0,0,0,.28);
  }
  .polaroid .shot { width: 100%; height: 100%; }
  .p1 { left: 140px; top: 281px; width: 295px; height: 314px; transform: rotate(-14deg); }
  .p1 .shot { background: linear-gradient(135deg, #8a5a3c, #e4c1a8 55%, #f3eeea); }
  .p2 { left: 441px; top: 274px; width: 300px; height: 290px; transform: rotate(15deg); }
  .p2 .shot { background: linear-gradient(135deg, #f2d2c4, #d8322f 45%, #f4f0ec 70%, #c02a2a); }
  .p3 { left: 266px; top: 525px; width: 250px; height: 285px; transform: rotate(8deg); }
  .p3 .shot { background: linear-gradient(150deg, #6d4a33, #efd0bb 50%, #f6e8df); }
  .p4 { left: 519px; top: 541px; width: 240px; height: 290px; transform: rotate(-20deg); }
  .p4 .shot { background: linear-gradient(150deg, #f7f5f2, #ecc9b5 50%, #f8f1ec); }

  .pin { position: absolute; width: 22px; height: 22px; border-radius: 50%;
    box-shadow: 1px 2px 3px rgba(0,0,0,.35); }
  .pin-red { background: radial-gradient(circle at 35% 35%, #ff6b6b, #c3121b); }
  .pin-blue { background: radial-gradient(circle at 35% 35%, #6fb7ff, #1554c4); }

  .price-sticker { position: absolute; left: 96px; top: 614px; width: 200px; height: 200px;
    filter: drop-shadow(0 3px 4px rgba(0,0,0,.25)); }
  .price-text {
    position: absolute; left: 96px; top: 664px; width: 200px; text-align: center;
    font-family: "Oswald", sans-serif; font-weight: 600; color: #fff;
    font-size: 50px; line-height: 48px;
  }

  .tagline {
    position: absolute; top: 948px; width: 100%; text-align: center;
    font-family: "Libre Baskerville", serif; font-weight: 700; font-size: 25px;
    letter-spacing: .5px; color: var(--ink);
  }
  .headline {
    position: absolute; top: 976px; width: 100%; text-align: center;
    font-family: "Lobster Two", cursive; font-style: italic; font-weight: 700;
    font-size: 82px; line-height: 90px; color: var(--red);
  }

  .features { position: absolute; top: 1092px; left: 0; width: 100%; }
  .feature { position: absolute; display: flex; align-items: center; gap: 10px; }
  .feature svg { width: 40px; height: 40px; }
  .feature span { font-weight: 600; font-size: 22px; line-height: 30px; color: var(--ink); }
  .f1 { left: 117px; } .f2 { left: 429px; } .f3 { left: 649px; }

  .footer-band { position: absolute; left: 0; bottom: 0; width: 100%; height: 14px; background: var(--teal); }
</style>
</head>
<body>
<main class="poster">
  <div class="decor decor-gift" role="img" aria-label="Red wrapped gift box with patterned ribbon bow and pine sprigs"></div>
  <div class="decor decor-greenery" role="img" aria-label="Fir branches with a frosted pine cone"></div>
  <div class="decor decor-present" role="img" aria-label="White wrapped present tied with twine"></div>

  <div class="brand">
    <div class="brand-dot"></div>
    <div class="brand-name">Coral Bay Grins</div>
  </div>

  <div class="polaroid p1"><div class="shot" role="img" aria-label="Smiling woman holding a glittering snowflake ornament"></div></div>
  <div class="polaroid p2"><div class="shot" role="img" aria-label="Close-up of a bright white smile with red lips"></div></div>
  <div class="polaroid p3"><div class="shot" role="img" aria-label="Excited woman with curly hair and a bright smile"></div></div>
  <div class="polaroid p4"><div class="shot" role="img" aria-label="Woman with a wide white smile"></div></div>

  <div class="pin pin-red" style="left:228px;top:284px"></div>
  <div class="pin pin-blue" style="left:628px;top:322px"></div>
  <div class="pin pin-blue" style="left:390px;top:522px"></div>
  <div class="pin pin-red" style="left:533px;top:560px"></div>

  <svg class="price-sticker" viewBox="0 0 200 200" aria-hidden="true">
    <path d="M197 126 A100 100 0 1 0 142 191 Q152 140 197 126 Z" fill="var(--sticker-red)"/>
    <path d="M197 126 Q160 128 150 152 Q142 172 142 191 Q182 172 197 126 Z" fill="var(--curl)"/>
  </svg>
  <div class="price-text">ONLY<br>$89</div>

  <p class="tagline">GIVE YOURSELF THE GIFT OF CHRISTMAS</p>
  <h1 class="headline">A Coral Bay Grin?</h1>

  <div class="features">
    <div class="feature f1">
      <svg viewBox="0 0 40 40" aria-hidden="true"><g stroke="var(--snow-blue)" stroke-width="3" stroke-linecap="round"><line x1="20" y1="3" x2="20" y2="37"/><line x1="5" y1="11.5" x2="35" y2="28.5"/><line x1="5" y1="28.5" x2="35" y2="11.5"/><path d="M15 6l5 4 5-4M15 34l5-4 5 4" fill="none"/></g></svg>
      <span>BRIGHTEN YOUR<br>HOLIDAY SMILE</span>
    </div>
    <div class="feature f2">
      <svg viewBox="0 0 40 40" aria-hidden="true"><g stroke="var(--snow-blue)" stroke-width="3" stroke-linecap="round"><line x1="20" y1="3" x2="20" y2="37"/><line x1="5" y1="11.5" x2="35" y2="28.5"/><line x1="5" y1="28.5" x2="35" y2="11.5"/><path d="M15 6l5 4 5-4M15 34l5-4 5 4" fill="none"/></g></svg>
      <span>INSTANT<br>RESULTS</span>
    </div>
    <div class="feature f3">
      <svg viewBox="0 0 40 40" aria-hidden="true"><g stroke="var(--snow-blue)" stroke-width="3" stroke-linecap="round"><line x1="20" y1="3" x2="20" y2="37"/><line x1="5" y1="11.5" x2="35" y2="28.5"/><line x1="5" y1="28.5" x2="35" y2="11.5"/><path d="M15 6l5 4 5-4M15 34l5-4 5 4" fill="none"/></g></svg>
      <span>FAMILY OWNED<br>AND OPERATED</span>
    </div>
  </div>

  <div class="footer-band"></div>
</main>
</body>
</html>
```